I need a label with logo to go on jars of honey.
Label size 70mm x 70mm
The front label should say :
The Tall Fern Honey Co. (logo)
Tarepo Honey
400g
The back label:
Would have nutritional information
And our address
You can see from the uploaded files the styles I prefer, I have uploaded a photo of the honey product too. The background of the logo doesn't have to be white. I would like to develop a color scheme that would look nice against the color of the honey.
Logo Text
The Tall Fern Honey Co. / The Tall Fern Honey Company

```html
<!DOCTYPE html>
<html lang="en">
<head>
<meta charset="utf-8">
<title>Tarepo Honey – Jar Labels</title>
<link href="https://fonts.googleapis.com/css2?family=Kaushan+Script&family=Roboto+Condensed:wght@400;700&family=Roboto:wght@700&display=swap" rel="stylesheet">
<style>
  :root{
    --brown:#5b3516;
    --brown-band:#6a3d1b;
    --honey:#f3b23a;
    --honey-soft:#f8c873;
    --motif:#fbe3c0;
    --paper:#ffffff;
    --badge:#3b3a39;
    --bg:#e4f3f3;
  }
  *{box-sizing:border-box;margin:0;padding:0}
  html,body{width:1000px;height:1200px;overflow:hidden;background:var(--bg)}
  .canvas{position:relative;width:1000px;height:1200px}
  .label{
    position:absolute;top:370px;width:460px;height:460px;
    background:var(--paper);border:7px solid var(--brown);border-radius:30px;overflow:hidden;
  }
  .label--front{left:26px}
  .label--back{left:514px}
  .motif{position:absolute;border-radius:50%;background:radial-gradient(circle,var(--motif) 0%,rgba(251,227,192,.35) 70%,rgba(251,227,192,0) 100%)}
  .motif--left{left:-90px;top:80px;width:220px;height:260px}
  .motif--right{right:-90px;top:130px;width:230px;height:260px}
  .product-name{
    position:absolute;font-family:"Kaushan Script",cursive;color:var(--brown);font-weight:400;
    text-shadow:4px 4px 0 var(--honey-soft);line-height:.95;transform:rotate(-13deg);transform-origin:left top;
    white-space:nowrap;
  }
  .label--front .product-name{left:36px;top:140px;font-size:96px}
  .label--front .product-name .line2{display:block;padding-left:84px}
  .label--back .product-name{left:112px;top:48px;font-size:54px;text-shadow:3px 3px 0 var(--honey-soft)}
  .label--back .product-name .line2{display:block;padding-left:50px}
  .maker{position:absolute;display:flex;align-items:center;gap:8px}
  .maker__dot{width:58px;height:58px;border-radius:50%;background:var(--badge);flex:none}
  .maker__name{font-family:"Roboto Condensed",sans-serif;font-weight:700;font-size:17px;color:var(--brown);line-height:1.1;width:90px}
  .label--front .maker{left:26px;bottom:40px}
  .label--back .maker{right:10px;bottom:22px;flex-direction:column;gap:4px;text-align:center;width:96px}
  .label--back .maker__dot{width:44px;height:44px}
  .label--back .maker__name{font-size:14px;width:96px}
  .bottler{
    position:absolute;right:8px;bottom:42px;width:218px;height:88px;background:var(--honey);
    clip-path:polygon(6% 8%,100% 0,98% 90%,0 100%,4% 55%);
    font-family:"Kaushan Script",cursive;color:#fff;text-align:right;padding:14px 20px 0 0;line-height:1.15;
  }
  .bottler__title{font-size:16px}
  .bottler__address{font-size:11px}
  .nutrition-title{position:absolute;left:40px;width:295px;top:142px;text-align:center;font-family:"Roboto",sans-serif;font-weight:700;font-size:17px;color:#111}
  .nutrition{position:absolute;left:40px;top:170px;width:295px;font-family:"Roboto Condensed",sans-serif;color:#111;font-size:16px}
  .nutrition__band{background:var(--brown-band);color:#fff;font-size:15px;padding:6px 8px;white-space:nowrap}
  .nutrition table{width:100%;border-collapse:collapse;border:1px solid #222;border-top:none}
  .nutrition td{vertical-align:top;padding:4px 7px;line-height:1.2;border-left:1px solid #222;white-space:nowrap}
  .nutrition td:first-child{border-left:none}
  .nutrition .head td{height:66px}
</style>
</head>
<body>
<main class="canvas">
  <section class="label label--front" aria-label="Front label">
    <div class="motif motif--left" role="img" aria-label="Faint Māori motif pattern"></div>
    <div class="motif motif--right" role="img" aria-label="Faint Māori motif pattern"></div>
    <h1 class="product-name"><span>Tarepo</span><span class="line2">Honey</span></h1>
    <div class="maker"><span class="maker__dot"></span><span class="maker__name">The Tall Fern Honey Co.</span></div>
    <div class="bottler" role="img" aria-label="Honey brush stroke with bottler details">
      <div class="bottler__title">Bottled by:<br>The Tall Fern Honey Co.</div>
      <div class="bottler__address">address or other company text</div>
    </div>
  </section>

  <section class="label label--back" aria-label="Back label">
    <div class="motif motif--left" role="img" aria-label="Faint Māori motif pattern"></div>
    <div class="motif motif--right" role="img" aria-label="Faint Māori motif pattern"></div>
    <h2 class="product-name"><span>Tarepo</span><span class="line2">Honey</span></h2>
    <div class="nutrition-title">NUTRITION INFORMATION</div>
    <div class="nutrition">
      <div class="nutrition__band">Serving per package: 20 Serving Size: 20 g</div>
      <table>
        <tr class="head"><td></td><td>Average<br>Quantity<br>per Serving</td><td>Average<br>Quantity per<br>100g</td></tr>
        <tr><td>Energy<br>Protein<br>Fat, total<br>- Saturated<br>Carbohydrate<br>- Sugars<br>Sodium</td>
            <td>272 kJ<br>0.08 g<br>0 g<br>0 g<br>15.9 g<br>15.6 g<br>2.4 mg</td>
            <td>1360 kJ<br>0.4 g<br>0 g<br>0 g<br>79.6 g<br>78.1 g<br>12 mg</td></tr>
      </table>
    </div>
    <div class="maker"><span class="maker__dot"></span><span class="maker__name">The Tall Fern Honey Co.</span></div>
  </section>
</main>
</body>
</html>
```